Popup Nightclub Grand Opening Flyer

We need to design a flyer for the grand opening of an upscale, exclusive nightclub called "Lanternfall". The design needs to be chic and exclusive. The background should be black and the text should primarily be white. We like minimalist designs.

Here is the text for the flyer
-
Velvetrope Atlanta Presents

Lanternfall (LOGO)

A Popup Nightclub Experience
For one night Only

Friday, October 18, 2013
Party begins at 9PM

INVITE ONLY

See invitation for location details
(Velvetrope Atlanta logo)

-
Examples we like

http://cdn2-b.brivelpost.com/sites/default/files/styles/image_content_width/hash/3d/fa/1472093815_4471_flyer.jpg?itok=R8kqWm2z

http://api.plovra.com/files/7Kqq-Tr82XXB3pQzJvmtR5HL2W719E4nbRtC6KLd4HsfM8Y2qTDK-VmjwDoNqLX4QBzTHD9nakRbVx3m-Pfq8htc3MDTWr5p4/2zelSaturdays.jpg

http://quenmar.com/wp-content/uploads/yootheme/widgetkit/gallery/2zel/2zel-gen_vroom4-01.jpg

Hi All, one thing that we are seeing that we don't like is on over emphasis on the phrase "a popup nightclub experience" please don't make this the largest thing on the flyer

Target Market(s)

Target market is 25-35 year olds who are affluent (rich) and like luxury brands

Requirements
Must have
• Dark Background
Nice to have
• Velvetrope Logo on the bottom
Modern text that isn't curvy
Should not have
• Curved text

```html
<!DOCTYPE html>
<html lang="en">
<head>
<meta charset="utf-8">
<title>Lanternfall Nightclub – Velvetrope Atlanta</title>
<link rel="stylesheet" href="https://fonts.googleapis.com/css2?family=Jura:wght@400;500&family=Quicksand:wght@400;500&display=swap">
<style>
  :root {
    --paper: #ffffff;
    --night: #050505;
    --night-soft: #161616;
    --ink: #f2f2f2;
    --ink-dim: #d8d8d8;
    --rule: rgba(255,255,255,0.85);
  }
  * { margin: 0; padding: 0; box-sizing: border-box; }
  html, body {
    width: 1000px; height: 1200px; overflow: hidden;
    background: var(--paper);
  }
  .flyer {
    position: absolute; left: 38px; top: 0;
    width: 925px; height: 1200px;
    background:
      radial-gradient(ellipse 60% 45% at 50% 42%, var(--night-soft), transparent 75%),
      linear-gradient(90deg, #0a0a0a, #111 30%, #0d0d0d 55%, #121212 80%, #080808);
    color: var(--ink);
    text-align: center;
    font-family: "Quicksand", sans-serif;
  }
  .flyer > * { position: absolute; left: 0; width: 100%; }
  .presenter { top: 28px; font-size: 22px; color: var(--ink-dim); }
  .brand-mark {
    top: 168px; left: 392px; width: 140px; height: 140px;
  }
  .brand-name {
    top: 365px; font-family: "Jura", sans-serif; font-weight: 400;
    font-size: 60px; letter-spacing: 9px; line-height: 1;
  }
  .brand-tag {
    top: 440px; font-family: "Jura", sans-serif; font-weight: 400;
    font-size: 29px; letter-spacing: 4px;
  }
  .tagline { top: 508px; font-size: 25px; line-height: 38px; color: var(--ink-dim); }
  .rule {
    height: 2px; left: 130px; width: 665px;
    background: linear-gradient(90deg, transparent, var(--rule) 20%, var(--rule) 80%, transparent);
  }
  .rule-top { top: 640px; }
  .rule-bottom { top: 801px; }
  .event-date {
    top: 664px; font-family: "Jura", sans-serif; font-weight: 500;
    font-size: 40px; line-height: 56px;
  }
  .access {
    top: 866px; font-family: "Jura", sans-serif; font-weight: 400;
    font-size: 68px; letter-spacing: 2px; line-height: 1;
  }
  .access-rule { top: 954px; left: 247px; width: 431px; height: 1px; background: var(--rule); }
  .access-note { top: 966px; font-size: 25px; letter-spacing: 0.5px; color: var(--ink-dim); }
  .host {
    top: 1075px; display: flex; justify-content: center; align-items: center; gap: 22px;
  }
  .host-dot { width: 52px; height: 52px; border-radius: 50%; background: var(--ink); }
  .host-name {
    font-family: "Quicksand", sans-serif; font-weight: 400;
    font-size: 36px; letter-spacing: 3px; line-height: 1;
  }
</style>
</head>
<body>
  <main class="flyer">
    <p class="presenter">Velvetrope Atlanta Presents</p>

    <svg class="brand-mark" viewBox="0 0 140 140" aria-hidden="true">
      <defs>
        <linearGradient id="silver" x1="0" y1="0" x2="1" y2="1">
          <stop offset="0" stop-color="#ffffff"/>
          <stop offset="1" stop-color="#9a9a9a"/>
        </linearGradient>
      </defs>
      <circle cx="70" cy="70" r="68" fill="url(#silver)"/>
    </svg>
    <h1 class="brand-name">LANTERNFALL</h1>
    <p class="brand-tag">NIGHTCLUB</p>

    <p class="tagline">A Popup Nightclub Experience<br>For one night Only</p>

    <div class="rule rule-top"></div>
    <p class="event-date">Friday, October 18, 2013<br>Party begins at 9PM</p>
    <div class="rule rule-bottom"></div>

    <h2 class="access">INVITE ONLY</h2>
    <div class="access-rule"></div>
    <p class="access-note">See invitation for location details</p>

    <div class="host">
      <span class="host-dot"></span>
      <span class="host-name">VELVETROPE ATLANTA</span>
    </div>
  </main>
</body>
</html>
```